依頼概要
■依頼の目的/概要
弊社の社員が着用する名札のデザインをお願いします。

■依頼詳細
社員全員が着用する名札を制作しようと考えております。
名札の素材はアクリルで検討していますが、デザインによって2層タイプのものにしたり、着色したりすることも検討しています。
名札はピン2本で固定しようと考えております。
名札を着用する服は、白のワイシャツ、白のブラウス及び緑色の作業ジャンパーです。

■デザインに必須の情報
名札に載せてほしい情報は、会社のロゴ、会社名及び個人の氏名です。
会社のロゴ及び社名は添付のファイルを参考にしてください。

■デザインに関する要望
シャープでかっちりした感じ、先進的な感じにしていただきたいです。

■弊社のご紹介
弊社は創業108年の住宅用資材を工務店や建設会社に販売する会社です。資材の販売を中心として、建築業界の生産性を向上させるためのシステム開発、各種教育システムの開発、地域の建築業界活性化に資する書籍の出版なども行っております。
社員数は100名、年商30億円の会社です。

その他何かご不明な点がございましたら、お気軽にご質問下さい。
よろしくお願いいたします。

シンプルながらしっかり我が社のイメージも出してくれるからです。しかも作業服に取り付ける場合のワッペンとしても作りやすいデザインでした。

短期間にもかかわらずたくさんのご提案ありがとうございました。
またいろいろとよろしくお願いします。

```html
<!DOCTYPE html>
<html lang="ja">
<head>
<meta charset="utf-8">
<title>名札デザイン</title>
<link rel="stylesheet" href="https://fonts.googleapis.com/css2?family=Noto+Sans+JP:wght@400;500;700&family=Roboto:wght@400&display=swap">
<style>
  :root {
    --page: #ffffff;
    --plate: #dcdcdc;
    --green: #1f9a3a;
    --green-light: #c7e6a4;
    --ink: #111111;
    --label: #222222;
  }
  html, body { margin: 0; padding: 0; overflow: hidden; }
  body {
    width: 704px; height: 1200px;
    background: var(--page);
    font-family: "Noto Sans JP", sans-serif;
    position: relative;
  }
  .variant { position: absolute; left: 97px; width: 500px; }
  .variant-label { font-size: 20px; color: var(--label); margin: 0 0 4px -4px; line-height: 1.2; }
  .plate { position: relative; width: 500px; height: 214px; background: var(--plate); overflow: hidden; }
  .plate-corner { position: absolute; left: 0; top: 0; }
  .company {
    position: absolute; right: 16px; top: 14px;
    display: flex; align-items: center; gap: 6px;
    color: var(--green); font-weight: 700;
  }
  .company-type { font-size: 11px; line-height: 1.1; width: 24px; text-align: center; }
  .company-name { font-size: 32px; letter-spacing: 2px; line-height: 1; }
  .romaji {
    position: absolute; top: 76px; left: 0; right: 0;
    font-family: "Roboto", sans-serif; font-size: 21px; color: var(--ink);
  }
  .romaji span { position: absolute; }
  .name {
    position: absolute; top: 104px; left: 0; right: 0;
    text-align: center; font-size: 62px; font-weight: 500; color: var(--ink);
    letter-spacing: 1px; line-height: 1.2;
  }
</style>
</head>
<body>

<section class="variant" style="top:70px">
  <p class="variant-label">【6文字】</p>
  <div class="plate">
    <svg class="plate-corner" width="200" height="200" viewBox="0 0 200 200">
      <polygon points="0,0 172,0 0,168" fill="var(--green-light)"/>
      <polygon points="172,0 188,0 0,184 0,168" fill="var(--green)"/>
      <circle cx="44" cy="48" r="24" fill="var(--green)"/>
    </svg>
    <div class="company"><span class="company-type">株式会社</span><span class="company-name">緑和</span></div>
    <div class="romaji"><span style="left:112px">Ookawara</span><span style="left:316px">Michiko</span></div>
    <div class="name">大河原 みち子</div>
  </div>
</section>

<section class="variant" style="top:326px">
  <p class="variant-label">【5文字】</p>
  <div class="plate">
    <svg class="plate-corner" width="200" height="200" viewBox="0 0 200 200">
      <polygon points="0,0 172,0 0,168" fill="var(--green-light)"/>
      <polygon points="172,0 188,0 0,184 0,168" fill="var(--green)"/>
      <circle cx="44" cy="48" r="24" fill="var(--green)"/>
    </svg>
    <div class="company"><span class="company-type">株式会社</span><span class="company-name">緑和</span></div>
    <div class="romaji"><span style="left:130px">Okamoto</span><span style="left:292px">Kenitiro</span></div>
    <div class="name">岡本 健一郎</div>
  </div>
</section>

<section class="variant" style="top:582px">
  <p class="variant-label">【4文字】</p>
  <div class="plate">
    <svg class="plate-corner" width="200" height="200" viewBox="0 0 200 200">
      <polygon points="0,0 172,0 0,168" fill="var(--green-light)"/>
      <polygon points="172,0 188,0 0,184 0,168" fill="var(--green)"/>
      <circle cx="44" cy="48" r="24" fill="var(--green)"/>
    </svg>
    <div class="company"><span class="company-type">株式会社</span><span class="company-name">緑和</span></div>
    <div class="romaji"><span style="left:140px">Higashino</span><span style="left:276px">Shuhei</span></div>
    <div class="name">東野 修平</div>
  </div>
</section>

<section class="variant" style="top:838px">
  <p class="variant-label">【3文字】</p>
  <div class="plate">
    <svg class="plate-corner" width="200" height="200" viewBox="0 0 200 200">
      <polygon points="0,0 172,0 0,168" fill="var(--green-light)"/>
      <polygon points="172,0 188,0 0,184 0,168" fill="var(--green)"/>
      <circle cx="44" cy="48" r="24" fill="var(--green)"/>
    </svg>
    <div class="company"><span class="company-type">株式会社</span><span class="company-name">緑和</span></div>
    <div class="romaji"><span style="left:166px">Takagi</span><span style="left:258px">Makoto</span></div>
    <div class="name">高木 誠</div>
  </div>
</section>

</body>
</html>
```